Sunny Hour Spirits Gin label

I’m looking for a gin label that as the title says it should be a bright and fun filled label for . The gin will have four seasons so each season will have a different label starting with a summer gin. It should be fright and cooler full happy and fun The name of the Gin is Sunny Hour Spirits Gin it should be bright and jump off the shelf.

Target Market(s)

Gin buyers

Font styles to use
Decorative
Script

Colors

Designer to choose colors to be used in the design.

Requirements
Must have
• Bright colours interesting eye catching

```html
<!DOCTYPE html>
<html lang="en">
<head>
<meta charset="utf-8">
<title>Sunny Hour Spirits Gin – Summer Label</title>
<link rel="stylesheet" href="https://fonts.googleapis.com/css2?family=Permanent+Marker&family=Pacifico&display=swap">
<style>
  :root {
    --page-bg: #ececec;
    --magenta: #d81b7a;
    --sun-yellow: #e6ee3a;
    --lagoon: #2fb5b0;
    --mango: #f59a1f;
    --violet: #6a4fc4;
    --panel-white: #ffffff;
    --title-fill: #93e6de;
    --title-stroke: #1e3b8c;
    --ink: #1b1b1b;
  }
  * { margin: 0; padding: 0; box-sizing: border-box; }
  html, body {
    width: 699px;
    height: 1200px;
    overflow: hidden;
    background: var(--page-bg);
  }
  .canvas {
    position: relative;
    width: 699px;
    height: 1200px;
  }
  .label {
    position: absolute;
    left: 40px;
    top: 213px;
    width: 620px;
    height: 773px;
    overflow: hidden;
  }
  .tropical-artwork {
    position: absolute;
    inset: 0;
    background:
      radial-gradient(circle at 85% 12%, var(--sun-yellow) 0 22%, transparent 23%),
      radial-gradient(circle at 12% 88%, var(--mango) 0 24%, transparent 25%),
      radial-gradient(circle at 80% 90%, var(--lagoon) 0 20%, transparent 21%),
      radial-gradient(circle at 8% 25%, var(--lagoon) 0 18%, transparent 19%),
      linear-gradient(135deg, var(--lagoon) 0%, var(--violet) 30%, var(--magenta) 55%, var(--mango) 80%, var(--sun-yellow) 100%);
  }
  .centre-panel {
    position: absolute;
    left: 79px;
    top: 180px;
    width: 460px;
    height: 360px;
    background: var(--panel-white);
    border: 3px solid var(--panel-white);
    outline: 2px solid rgba(255,255,255,0.8);
    outline-offset: 8px;
    transform: rotate(-4deg);
  }
  .category {
    position: absolute;
    left: 172px;
    top: 56px;
    font-family: "Permanent Marker", cursive;
    font-size: 58px;
    color: var(--ink);
    line-height: 1;
  }
  .product-name {
    position: absolute;
    left: 60px;
    top: 120px;
    width: 520px;
    font-family: "Pacifico", cursive;
    color: var(--title-fill);
    -webkit-text-stroke: 5px var(--title-stroke);
    paint-order: stroke fill;
    text-shadow: 4px 5px 0 var(--title-stroke);
    transform: rotate(-6deg);
    line-height: 1.05;
  }
  .product-name span { display: block; }
  .product-name .line-1 { font-size: 96px; margin-left: 20px; }
  .product-name .line-2 { font-size: 96px; margin-left: 90px; }
  .product-name .line-3 { font-size: 96px; margin-left: 110px; }
  .strength {
    position: absolute;
    left: 88px;
    top: 622px;
    font-family: "Permanent Marker", cursive;
    font-size: 34px;
    line-height: 1.05;
    color: var(--ink);
    transform: rotate(8deg);
  }
  .maker {
    position: absolute;
    left: 318px;
    top: 622px;
    font-family: "Permanent Marker", cursive;
    font-size: 36px;
    line-height: 1.05;
    color: var(--ink);
    text-align: right;
    transform: rotate(-6deg);
  }
</style>
</head>
<body>
  <main class="canvas">
    <section class="label">
      <div class="tropical-artwork" role="img" aria-label="Tropical illustration of palm leaves, monstera leaves and flowers in teal, violet, magenta, yellow and orange"></div>
      <div class="centre-panel"></div>
      <p class="category">GIN</p>
      <h1 class="product-name">
        <span class="line-1">Sunny</span>
        <span class="line-2">Hour</span>
        <span class="line-3">Spirits</span>
      </h1>
      <p class="strength">42%<br>ABC</p>
      <p class="maker">CLAWFOOT<br>GIN CO</p>
    </section>
  </main>
</body>
</html>
```